Brand Identity Stationary Package

Hello I'm looking for a full branding package for my Property Management Company. I have a logo but looking to have the following
Business Card
Email signature
Facebook cover photo
Letterhead (word.doc)
#10 Envelope
Pocket Folder - link to 9x12 pocket folder design specs https://www.plorafine.ca/marketing-materials/presentation-folders
would like everything to match and be brand identifiable. The company looks after residential properties/apartments and some commercial properties. Attached is a zip of the files.
For Business Card
Name: Gideon Falkner
Position: Operations Manager
Number: 1 (506) 384-2917
Email: Gideon@quarrytide.ca
Website: Quarrytide.ca
Property Management

```html
<!DOCTYPE html>
<html lang="en">
<head>
<meta charset="utf-8">
<title>Quarrytide Business Card</title>
<link rel="stylesheet" href="https://fonts.googleapis.com/css2?family=Poppins:wght@400;600;700&display=swap">
<style>
  :root {
    --page-bg: #1c1c1d;
    --card-bg: #2c2c2d;
    --card-shade: #242425;
    --brand-green: #6cb52d;
    --silver: #d9d9d9;
    --text-light: #f2f2f2;
    --muted: #9a9a9a;
  }
  * { box-sizing: border-box; margin: 0; padding: 0; }
  html, body { width: 1200px; height: 874px; overflow: hidden; background: var(--page-bg); }
  body { font-family: "Poppins", sans-serif; position: relative; }

  .card {
    position: absolute;
    left: 310px;
    width: 580px;
    height: 331px;
    background: var(--card-bg);
    border-radius: 22px;
    overflow: hidden;
  }
  .card--front { top: 86px; }
  .card--back  { top: 457px; }

  .brand {
    position: absolute;
    left: 0; right: 0; top: 118px;
    text-align: center;
  }
  .brand__name {
    display: flex; align-items: center; justify-content: center; gap: 14px;
    font-weight: 700; font-size: 50px; letter-spacing: 4px;
    color: var(--brand-green); line-height: 1;
  }
  .brand__dot { width: 14px; height: 14px; background: var(--brand-green); }
  .brand__tagline {
    margin-top: 12px;
    font-weight: 400; font-size: 12px; letter-spacing: 7px;
    color: var(--muted); text-transform: uppercase;
  }

  .back__art { position: absolute; left: 0; top: 0; width: 330px; height: 331px; }

  .contact {
    position: absolute;
    right: 40px; top: 96px;
    text-align: right;
  }
  .contact__name { font-weight: 600; font-size: 27px; color: var(--brand-green); line-height: 1.1; }
  .contact__role { font-size: 15px; font-style: normal; color: var(--text-light); margin-bottom: 16px; }
  .contact__list { list-style: none; }
  .contact__item {
    display: flex; align-items: center; justify-content: flex-end; gap: 10px;
    font-size: 15px; color: var(--text-light); line-height: 1.45;
  }
  .contact__icon { width: 13px; height: 13px; flex: none; }
</style>
</head>
<body>

<section class="card card--front" aria-label="Card front">
  <div class="brand">
    <div class="brand__name"><span class="brand__dot"></span>QUARRYTIDE</div>
    <div class="brand__tagline">Property Management</div>
  </div>
</section>

<section class="card card--back" aria-label="Card back">
  <svg class="back__art" viewBox="0 0 330 331" role="img" aria-label="Large grey decorative brand shape area">
    <defs>
      <linearGradient id="artShade" x1="0" y1="0" x2="1" y2="1">
        <stop offset="0" stop-color="#6a6a6b"/>
        <stop offset="0.55" stop-color="#3a3a3b"/>
        <stop offset="1" stop-color="#1f1f20"/>
      </linearGradient>
    </defs>
    <polygon points="0,110 210,60 330,331 0,331" fill="url(#artShade)"/>
  </svg>

  <div class="contact">
    <h1 class="contact__name">Gideon Falkner</h1>
    <p class="contact__role"><em>Operations Manager</em></p>
    <ul class="contact__list">
      <li class="contact__item">1 (506) 384-2917
        <svg class="contact__icon" viewBox="0 0 24 24" aria-hidden="true"><path fill="#6cb52d" d="M6.6 10.8a15 15 0 0 0 6.6 6.6l2.2-2.2a1 1 0 0 1 1-.25 11.4 11.4 0 0 0 3.6.57 1 1 0 0 1 1 1V20a1 1 0 0 1-1 1A17 17 0 0 1 3 4a1 1 0 0 1 1-1h3.5a1 1 0 0 1 1 1c0 1.25.2 2.45.57 3.57a1 1 0 0 1-.25 1z"/></svg>
      </li>
      <li class="contact__item">Gideon@quarrytide.ca
        <svg class="contact__icon" viewBox="0 0 24 24" aria-hidden="true"><rect x="2" y="5" width="20" height="14" rx="1.5" fill="#6cb52d"/><path d="M3 6l9 7 9-7" fill="none" stroke="#2c2c2d" stroke-width="2"/></svg>
      </li>
      <li class="contact__item">www.Quarrytide.ca
        <svg class="contact__icon" viewBox="0 0 24 24" aria-hidden="true"><circle cx="12" cy="12" r="10" fill="#6cb52d"/><path d="M2 12h20M12 2c3 3 3 17 0 20M12 2c-3 3-3 17 0 20" fill="none" stroke="#2c2c2d" stroke-width="1.6"/></svg>
      </li>
    </ul>
  </div>
</section>

</body>
</html>
```